Statistical Data Science Lab website landing graphic

My lab (http://research.brantleymoor.org/lenz) develops novel statistical and computational tools for analyzing and making sense of complex genomic data. I am looking for a graphic to replace the boring/generic image that is on the landing page of my website. I want something that has the words "Lenz Group" in the center with images (possibly translucent) in the background that reflect the projects that we work on in terms of using complex math and computation to analyze data from genomics and the human microbiome (bacteria in poop) studies of various diseases. The colors should mesh with the remainder of the website.

```html
<!DOCTYPE html>
<html lang="en">
<head>
<meta charset="utf-8">
<title>Lenz Group</title>
<link rel="stylesheet" href="https://fonts.googleapis.com/css2?family=Arimo:ital,wght@0,400;0,700;1,700&family=Bebas+Neue&display=swap">
<style>
  :root {
    --navy: #1d3461;
    --ink: #111111;
    --white: #ffffff;
    --hero-deep: #1f3f7a;
    --hero-mid: #2d5ea3;
    --hero-light: #3f7fc0;
    --line-grey: #9aa3b3;
  }
  * { box-sizing: border-box; margin: 0; padding: 0; }
  html, body {
    width: 1200px; height: 900px; overflow: hidden;
    background: var(--white);
    font-family: "Arimo", Arial, sans-serif;
    color: var(--ink);
  }
  .page { position: relative; width: 1200px; height: 900px; overflow: hidden; }

  .site-header { position: absolute; left: 0; top: 0; width: 100%; height: 90px; }
  .brand {
    position: absolute; left: 88px; top: 28px;
    display: flex; align-items: center; gap: 8px;
    font-weight: 700; font-size: 26px; color: var(--navy);
  }
  .brand-mark { width: 12px; height: 12px; background: var(--navy); }
  .main-nav { position: absolute; left: 357px; top: 39px; display: flex; gap: 36px; }
  .main-nav a { font-size: 12px; color: var(--navy); text-decoration: none; }
  .search {
    position: absolute; left: 955px; top: 36px; width: 156px; height: 18px;
    border: 1.5px solid var(--navy); border-radius: 9px;
    display: flex; align-items: center; font-size: 11px; color: var(--line-grey);
  }
  .search-icon { width: 24px; height: 100%; border-right: 1px solid var(--navy); display: flex; align-items: center; justify-content: center; }
  .search-text { padding-left: 7px; }

  .hero-art {
    position: absolute; left: -90px; top: 142px; width: 610px; height: 610px;
    border-radius: 50%;
    background: radial-gradient(circle at 45% 40%, var(--hero-light) 0%, var(--hero-mid) 45%, var(--hero-deep) 100%);
  }
  .hero-title {
    position: absolute; left: 54px; top: 404px;
    font-family: "Bebas Neue", "Arial Narrow", sans-serif;
    font-size: 108px; line-height: 1; color: var(--white); letter-spacing: 0.5px;
  }

  .welcome {
    position: absolute; left: 602px; top: 190px; width: 518px; text-align: center;
  }
  .welcome h1 { font-size: 26px; font-weight: 700; line-height: 30px; margin-bottom: 8px; }
  .welcome p { font-size: 16.6px; line-height: 19px; margin-bottom: 19px; }
  .welcome em { font-weight: 700; }

  .actions { position: absolute; left: 766px; top: 579px; display: flex; gap: 20px; }
  .btn {
    width: 86px; height: 35px; border-radius: 8px;
    font-family: "Bebas Neue", "Arial Narrow", sans-serif; font-size: 15px;
    display: flex; align-items: center; justify-content: center;
    border: 2px solid var(--navy);
  }
  .btn-donate { background: var(--navy); color: var(--white); }
  .btn-fundraise { background: var(--white); color: var(--navy); }

  .partner {
    position: absolute; left: 704px; top: 672px;
    display: flex; align-items: center; gap: 16px;
    font-weight: 700; color: var(--navy);
  }
  .partner-mark { width: 60px; height: 60px; border-radius: 50%; background: var(--navy); flex: none; }
  .partner-name { display: flex; flex-direction: column; }
  .partner-name-main { font-size: 38px; line-height: 42px; }
  .partner-name-sub { font-size: 24px; line-height: 26px; }
</style>
</head>
<body>
<div class="page">
  <header class="site-header">
    <div class="brand"><span class="brand-mark"></span>Lenz's Group</div>
    <nav class="main-nav">
      <a href="#">Daniel R. Lenz, P.I.</a>
      <a href="#">Group Members</a>
      <a href="#">Research</a>
      <a href="#">Software</a>
      <a href="#">Publications</a>
    </nav>
    <div class="search">
      <span class="search-icon">
        <svg width="11" height="11" viewBox="0 0 12 12"><circle cx="5" cy="5" r="3.6" fill="none" stroke="#1d3461" stroke-width="1.5"/><line x1="7.6" y1="7.6" x2="11" y2="11" stroke="#1d3461" stroke-width="1.6"/></svg>
      </span>
      <span class="search-text">e.g. Leukemia</span>
    </div>
  </header>

  <div class="hero-art" role="img" aria-label="Blue-tinted microscope photograph of rod-shaped gut bacteria inside a circle, with colourful diagonal bars"></div>
  <div class="hero-title">LENZ GROUP</div>

  <section class="welcome">
    <h1>Welcome to our group homepage!</h1>
    <p><em>Daniel Lenz</em> is a Professor in the Biostatistics Program, Public Health Sciences Division, Brantley Moor Research Center. The major thrust of the group's research lies in the development and application of statistical methods for for analysis of high-dimensional genomic data within the broader context of clinical trials as well as population-based genetic, genomic, epigenetic, and microbiome studies. Currently, the group is heavily invested in developing and applying cutting edge approaches for microbiome and metagenomic studies. Applications focus a range of additional conditions, disorders, disease and contexts include aging, autoimmune disorders, cancer, cardiovascular disease, environmental health, and reproductive/perinatal outcomes.</p>
    <p>We are always eager to develop new collaborations with investigators within substantive fields as well as methodological researchers.</p>
  </section>

  <div class="actions">
    <div class="btn btn-donate">DONATE</div>
    <div class="btn btn-fundraise">FUNDRAISE</div>
  </div>

  <div class="partner">
    <span class="partner-mark"></span>
    <span class="partner-name">
      <span class="partner-name-main">Brantley Moor</span>
      <span class="partner-name-sub">Research Center</span>
    </span>
  </div>
</div>
</body>
</html>
```